Rabbit Meat Label

We need a label for a shrink-wrapped tray of rabbit. The label does not need to be fancy, we just want a simple sticker to show customers a mock-up of what it may look like. The label is approximately 5" x 2.75". The label will go on top of the rabbit, so it will not lay flat. Please take that into consideration

The rabbit specifically is farm raised. Whole cut-up with 2 fore-legs, 2 hind legs and back.

There is nutritional information on the back, so please mention that somewhere on the label.

Industry/Entity Type

Farm

Requirements
Must have
• Please leave spaces for FQRB seals and other misc items. They are about 0.5" squares.
Should not have
• Do not have anything like "Made in the USA" or "All Natural." This will be added later, if need be.

```html
<!DOCTYPE html>
<html lang="en">
<head>
<meta charset="utf-8">
<title>Farm Raised Rabbit – Tray Label</title>
<link rel="stylesheet" href="https://fonts.googleapis.com/css2?family=Arimo:wght@400;700&display=swap">
<style>
  :root {
    --label-cream: #ebe7c6;
    --label-cream-light: #f1edd2;
    --brand-maroon: #581315;
    --ink: #000000;
    --rule-grey: #a3a3a0;
  }
  html, body {
    margin: 0;
    padding: 0;
    overflow: hidden;
    background: var(--label-cream);
  }
  .label {
    position: relative;
    width: 1200px;
    height: 660px;
    overflow: hidden;
    background: var(--label-cream);
    font-family: "Arimo", Arial, sans-serif;
  }
  .label__art,
  .label__type {
    position: absolute;
    inset: 0;
    width: 1200px;
    height: 660px;
  }
  .title-small   { font-size: 80px; fill: var(--ink); }
  .title-large   { font-size: 172px; fill: var(--brand-maroon); }
  .cut-line      { font-size: 61px; fill: var(--ink); }
  .cut-count     { font-size: 102px; fill: var(--brand-maroon); }
  .cut-part      { font-size: 44px; fill: var(--ink); }
  .cut-back      { font-size: 72px; fill: var(--ink); }
  .back-note     { font-size: 24px; fill: var(--ink); }
  .rule          { fill: var(--ink); }
  .rule-dotted   { stroke: var(--rule-grey); stroke-width: 5; stroke-dasharray: 7 9; }
  .brand-band    { fill: var(--brand-maroon); }
</style>
</head>
<body>
  <main class="label">
    <svg class="label__art" viewBox="0 0 1200 660" aria-hidden="false">
      <defs>
        <linearGradient id="silhouetteTone" x1="0" y1="0" x2="0" y2="1">
          <stop offset="0" stop-color="var(--label-cream-light)"/>
          <stop offset="1" stop-color="var(--label-cream)"/>
        </linearGradient>
      </defs>
      <polygon class="brand-band" points="744,0 1200,0 1200,660 832,660"/>
      <rect class="rabbit-silhouette" x="860" y="40" width="340" height="540" rx="40"
            fill="url(#silhouetteTone)" role="img"
            aria-label="Cream silhouette of a sitting rabbit in profile, facing left"/>
    </svg>

    <svg class="label__type" viewBox="0 0 1200 660">
      <rect class="rule" x="100" y="22" width="476" height="18"/>
      <text class="title-small" x="102" y="116" textLength="467" lengthAdjust="spacingAndGlyphs">Farm Raised</text>
      <text class="title-large" x="96" y="252" textLength="480" lengthAdjust="spacingAndGlyphs">Rabbit</text>
      <line class="rule-dotted" x1="103" y1="266" x2="572" y2="266"/>
      <text class="cut-line" x="97" y="324" textLength="479" lengthAdjust="spacingAndGlyphs">Whole cut-up with</text>
      <text class="cut-count" x="96" y="418">2</text>
      <text class="cut-part" x="174" y="376" textLength="170" lengthAdjust="spacingAndGlyphs">forelegs</text>
      <text class="cut-part" x="174" y="416" textLength="170" lengthAdjust="spacingAndGlyphs">hind legs</text>
      <text class="cut-back" x="352" y="406" textLength="226" lengthAdjust="spacingAndGlyphs">&amp; back</text>
      <rect class="rule" x="99" y="433" width="479" height="18"/>
      <text class="back-note" x="112" y="644" textLength="462" lengthAdjust="spacingAndGlyphs">See nutritional information on the back</text>
    </svg>
  </main>
</body>
</html>
```